Brochure Design Project

We need a brochure design, copy writing and print ready art for a Toronto based commercial cleaning company. Output should be an 8.5X11 four page piece.

We provide "green cleaning" - environmentally friendly cleaning programs. Our positioning is strongly environmentally oriented, high quality, reliable and affordable.

We provide interior cleaning for office buildings, condominiums, manufacturing facilities, gyms, retail stores, daycares, churches and banquet facilities.

Core services are; regularly scheduled cleaning programs, floor maintenance, carpet cleaning, window cleaning, construction cleaning and sanitary supply management.

Looking for a "fresh" clean look that screams "competent" and "professional" and clearly communicates "affordability"

The piece will be used as a stand alone mailer and leave behind for a salesperson.

Reason: Designs have not met the brief specifications

Target Market(s)

Mid level managers of virtually every "non food service" company, facility or operation. Slightly skewed to female decision makers

Industry/Entity Type

Construction

Requirements
Must have
• Clear identification of the key services with image support, ie floor maintenance image, carpet cleaning

```html
<!DOCTYPE html>
<html lang="en">
<head>
<meta charset="utf-8">
<title>Green Cleaning Brochure</title>
<link rel="stylesheet" href="https://fonts.googleapis.com/css2?family=Noto+Sans:wght@400;700&family=Noto+Serif:wght@400&display=swap">
<style>
  :root {
    --leaf: #8cbb2f;
    --forest: #1d5a2c;
    --ink: #1f3b24;
    --paper: #ffffff;
    --frame: #2c5a33;
    --sky: #bfe0f5;
    --water: #3f8fd0;
    --meadow: #a9c94a;
  }
  * { box-sizing: border-box; margin: 0; padding: 0; }
  html, body { width: 1200px; height: 848px; overflow: hidden; background: var(--paper); }
  body { font-family: "Noto Sans", Arial, sans-serif; color: var(--ink); }

  .brochure { position: relative; width: 1200px; height: 848px; display: flex; }
  .panel { position: relative; height: 848px; text-align: center; }
  .panel--services { width: 400px; }
  .panel--values { width: 398px; border-left: 1px solid #d8d8d8; }
  .panel--cover { width: 402px; }

  .band { position: absolute; left: 0; width: 400px; background: var(--leaf); }
  .band--top { top: 0; height: 78px; }
  .band--bottom { bottom: 0; height: 74px; }

  .section-title { color: var(--forest); font-weight: 700; font-size: 21px; line-height: 1.2; }
  .list { list-style: none; font-size: 16.5px; line-height: 25.8px; color: var(--ink); }

  .clients { position: absolute; top: 98px; left: 0; width: 400px; }
  .clients .list { margin-top: 2px; }
  .services { position: absolute; top: 340px; left: 0; width: 400px; }
  .services .list { margin-top: 4px; }

  .art { position: absolute; }
  .art--supplies {
    left: 92px; top: 540px; width: 222px; height: 290px; border-radius: 14px;
    background: radial-gradient(ellipse at 50% 45%, #c9e27a 0%, #8fbf3a 55%, #5f9a2b 100%);
  }
  .art--globe {
    left: 56px; top: 54px; width: 288px; height: 288px; border-radius: 50%;
    background: radial-gradient(circle at 45% 45%, #cfe9fb 0%, #5aa6dd 45%, #7fbf3a 80%, #ffffff 100%);
  }

  .values { position: absolute; top: 372px; left: 0; width: 398px; }
  .values .section-title { font-size: 20px; line-height: 25px; }
  .values .list { margin-top: 4px; }

  .contact {
    position: absolute; left: 46px; top: 570px; width: 310px; height: 260px;
    border: 1.5px solid var(--frame); padding-top: 12px;
    font-size: 15px; line-height: 19px; color: var(--ink);
  }
  .contact__online { margin-top: 9px; }
  .contact__web { margin-top: 8px; font-weight: 700; letter-spacing: 2.6px; font-size: 14.5px; }
  .company-name {
    margin-top: 22px; display: flex; align-items: center; justify-content: center; gap: 8px;
    font-size: 14px; font-weight: 700; letter-spacing: 1.4px; color: var(--leaf);
  }
  .company-name__dot { width: 12px; height: 12px; border-radius: 50%; background: var(--leaf); }

  .art--meadow {
    left: 0; top: 0; width: 402px; height: 848px;
    background: linear-gradient(180deg, #ffffff 0%, #f4f8df 12%, #dfeaa4 30%, var(--meadow) 48%, #c5dc7a 58%, #eef6f4 68%, var(--sky) 76%, #7fb8e6 88%, #e5f2fb 100%);
  }
  .cover-title {
    position: absolute; top: 74px; left: 0; width: 402px;
    font-family: "Noto Serif", Georgia, serif; font-weight: 400; font-size: 45px;
    color: var(--forest); line-height: 1;
  }
  .cover-intro {
    position: absolute; top: 148px; left: 14px; width: 374px;
    font-size: 15.5px; line-height: 22px; color: var(--ink);
  }
  .cover-intro strong { font-weight: 700; }
</style>
</head>
<body>
<main class="brochure">
  <section class="panel panel--services">
    <div class="band band--top"></div>
    <div class="clients">
      <h2 class="section-title">We provide interior cleaning for</h2>
      <ul class="list">
        <li>Office buildings</li><li>Condominiums</li><li>Manufacturing facilities</li><li>Gyms</li>
        <li>Retail stores</li><li>Daycares</li><li>Churches</li><li>Banquet facilities</li>
      </ul>
    </div>
    <div class="services">
      <h2 class="section-title">Our Services</h2>
      <ul class="list">
        <li>Regularly scheduled cleaning programs</li><li>Floor maintenance</li><li>Carpet cleaning</li>
        <li>Window cleaning</li><li>Construction cleaning</li><li>Sanitary supply management</li>
      </ul>
    </div>
    <div class="art art--supplies" role="img" aria-label="Green basket filled with cleaning bottles, sponges, cloth and duster"></div>
    <div class="band band--bottom"></div>
  </section>

  <section class="panel panel--values">
    <div class="art art--globe" role="img" aria-label="Blue globe wrapped in fresh green leaves with water droplets"></div>
    <div class="values">
      <h2 class="section-title">Professional Facility<br>Management &amp; Maintenance</h2>
      <ul class="list">
        <li>Dependability</li><li>Integrity</li><li>Quality</li><li>Affordability</li><li>Environmental Responsibility</li>
      </ul>
    </div>
    <address class="contact" style="font-style: normal;">
      <p>Verdant Facility Care Inc.</p>
      <p>1280 Birchmount Road</p>
      <p>Unit 5</p>
      <p>Oakridge, Ontario</p>
      <p>K2P 4M7</p>
      <p class="contact__online">Visit us online at</p>
      <p class="contact__web">www.verdantcare.ca</p>
      <p class="company-name"><span class="company-name__dot"></span>VERDANT FACILITY CARE</p>
    </address>
  </section>

  <section class="panel panel--cover">
    <div class="art art--meadow" role="img" aria-label="Sunlit meadow of white daisies above a clear blue water surface with bubbles"></div>
    <h1 class="cover-title">Green Cleaning</h1>
    <p class="cover-intro">We provide <strong>"green cleaning"</strong> Environmentally friendly cleaning programs. Our positioning is strongly environmentally oriented, high quality, reliable and affordable.</p>
  </section>
</main>
</body>
</html>
```